■依頼目的/概要
電子書籍を出版しますので、
表紙デザイン作成をお願いいたします。

■本のタイトル
ソラトビ!
~金沢発 16才女子高生社長の海外体験記~

<著者>株式会社七海舎 代表取締役社長 柴田遥香
※参考に株式会社七海舎 の社名ロゴを添付します。

■本の内容

「株式会社七海舎」の代表取締役社長である
著者、柴田遥香さんが、
海外で感じた事や、

高校生でありながら起業に至る経緯などを、
JKらしい軽快な文体で本にしました。

※参考に本の原稿を資料として添付します。

高校2年生の海外渡航体験で、
東南アジアのエネルギーを
目の当たりにしたことをきっかけに、

「日本の元気のなさってヤバくない?」
「もっと10代のうちに海外を見ようよ!」
と、心の底から感じました。

その思いを形にすべく、現在は、
10代向け海外留学支援サイト「ソラトビ!」を、
立ち上げ運営しています。サイトはこちらです。

https://soratobi-site.example/profile/
※ソラトビ!ロゴを参考材料として添付します。

■デザイン要望

16才の遥香社長の元気でチャレンジャーな感じを表現したいです。

できれば、
遥香さんの写真を使いたいと思っています。

※遥香さんの写真を材料として添付します。
※株式会社七海舎の会社ロゴ、
および運営サイト「ソラトビ!」のロゴも参考に添付しますので、
使用についてはデザイナーさんにお任せします。

その他の
イラストや写真等素材を使用される場合には、
商用利用可の素材をお願いします。

色合い、デザインレイアウトとも、
デザイナーさんにお任せしたいと思います。

■その他、デザインを考えるのに必要な情報などありましたら、
お答えしますので、遠慮なく聞いて下さい。

※添付資料
・遥香社長の写真
・株式会社七海舎のロゴ画像
・留学サイト「ソラトビ!」のロゴ
・原稿たたき
素晴らしいご提案をいただきありがとうございます。
提案予約のご連絡をいただきましたため、
締切日時を2日だけ延長させていただきます。

引き続き、よろしくお願いいたします。

かなり悩みましたが、
ぱっとみてわかりやすい、
ロゴにインパクトがあった、
パブリックな感じがポイントになりました。

この度はご提案いただきありがとうございました。
たくさんのいい提案があり、選考に本当に迷いました。
ご応募してくださったワーカーのみなさまに感謝いたします。

また依頼することもあるかと思いますので、
その時はよろしくお願いいたします。

```html
<!DOCTYPE html>
<html lang="ja">
<head>
<meta charset="utf-8">
<title>ソラトビ! 表紙</title>
<link href="https://fonts.googleapis.com/css2?family=M+PLUS+Rounded+1c:wght@500;800;900&display=swap" rel="stylesheet">
<style>
  :root {
    --brown: #5a3418;
    --orange: #f08a16;
    --sky: #2fb3e3;
    --green: #22a03c;
    --white: #ffffff;
    --photo-top: #9fc7e6;
    --photo-mid: #b06a4a;
    --photo-low: #8a7a66;
  }
  html, body { margin: 0; padding: 0; overflow: hidden; background: #fff; }
  .cover {
    position: relative;
    width: 750px; height: 1200px;
    overflow: hidden;
    background: var(--white);
    font-family: "M PLUS Rounded 1c", sans-serif;
    color: var(--brown);
  }
  .cover-photo {
    position: absolute; left: 0; top: 0; width: 750px; height: 760px;
    background: linear-gradient(180deg, var(--photo-top) 0%, #d9c2b0 28%, var(--photo-mid) 48%, #c9a58a 70%, var(--photo-low) 100%);
    clip-path: polygon(0 0, 100% 0, 100% 88%, 0 100%);
  }
  .backdrop { position: absolute; inset: 0; }
  .airplane {
    position: absolute; left: 615px; top: 40px;
    width: 120px; height: 110px; border-radius: 50%;
    background: radial-gradient(circle, rgba(255,255,255,.95) 0%, rgba(255,255,255,.6) 55%, rgba(255,255,255,0) 72%);
  }
  .tagline {
    position: absolute; left: 30px; top: 22px;
    background: var(--white); border-radius: 40px;
    padding: 12px 26px; font-weight: 800; font-size: 34px; letter-spacing: 1px;
  }
  .tagline::after {
    content: ""; position: absolute; left: 60px; bottom: -16px;
    border: 10px solid transparent; border-top: 10px solid var(--white);
  }
  .origin-badge {
    position: absolute; left: 565px; top: 400px;
    background: var(--green); color: var(--white);
    font-weight: 900; font-size: 36px; padding: 6px 18px;
    border: 5px solid var(--white); border-radius: 14px;
    transform: rotate(-8deg);
  }
  .subtitle { position: absolute; left: 40px; top: 440px; }
  .age-badge {
    display: inline-flex; align-items: center; justify-content: center;
    width: 82px; height: 82px; border-radius: 50%;
    background: var(--orange); color: var(--white);
    border: 5px solid var(--white); font-weight: 900; font-size: 34px;
    vertical-align: middle;
  }
  .subtitle-line {
    font-weight: 900; paint-order: stroke fill;
    -webkit-text-stroke: 12px var(--white);
  }
  .subtitle-role { color: var(--orange); font-size: 62px; vertical-align: middle; }
  .subtitle-topic { display: block; margin: 4px 0 0 205px; color: var(--brown); font-size: 66px; }
  .title {
    position: absolute; left: 20px; top: 620px; margin: 0;
    font-weight: 900; color: var(--brown); line-height: 1;
    paint-order: stroke fill; -webkit-text-stroke: 16px var(--white);
  }
  .title-top { display: block; font-size: 210px; letter-spacing: 4px; transform: rotate(-5deg); transform-origin: left center; }
  .title-bottom { display: block; font-size: 200px; margin: 10px 0 0 170px; }
  .visually-hidden {
    position: absolute; width: 1px; height: 1px; overflow: hidden; clip: rect(0 0 0 0);
  }
  .arrow { position: absolute; left: 625px; top: 590px; }
  .author { position: absolute; left: 28px; bottom: 36px; color: var(--white); }
  .author-org { font-size: 24px; font-weight: 800; line-height: 1.25; }
  .author-name {
    position: absolute; left: 230px; bottom: 0; white-space: nowrap;
    font-size: 48px; font-weight: 900; letter-spacing: 4px;
  }
</style>
</head>
<body>
<div class="cover">
  <div class="cover-photo" role="img" aria-label="金沢駅の鼓門の前でジャンプする制服姿の女子高生の写真"></div>

  <svg class="backdrop" width="750" height="1200" viewBox="0 0 750 1200" aria-hidden="true">
    <polygon points="0,1030 750,790 750,1200 0,1200" fill="var(--sky)"/>
    <polygon points="0,770 180,730 180,790 0,830" fill="var(--sky)"/>
  </svg>

  <div class="airplane" role="img" aria-label="空へ飛び立つ白い飛行機のイラスト"></div>

  <div class="tagline">10代よ、世界へ飛び出せ!</div>
  <div class="origin-badge">金沢発!</div>

  <div class="subtitle">
    <span class="age-badge">16才</span>
    <span class="subtitle-line subtitle-role">女子高生社長の</span>
    <span class="subtitle-line subtitle-topic">海外体験記</span>
  </div>

  <h1 class="title">
    <span class="title-top">ソラ</span>
    <span class="title-bottom">トビ<span class="visually-hidden">!</span></span>
  </h1>

  <svg class="arrow" width="110" height="470" viewBox="0 0 110 470" aria-hidden="true">
    <polygon points="55,4 106,118 72,108 68,462 42,462 38,108 4,118" fill="var(--orange)" stroke="var(--white)" stroke-width="6" stroke-linejoin="round"/>
  </svg>

  <div class="author">
    <div class="author-org">株式会社七海舎<br>代表取締役社長</div>
    <div class="author-name">柴田遥香</div>
  </div>
</div>
</body>
</html>
```